Tapfold Nest mobile app; beer delivery service

We are looking for a design of our app - "Tapfold Nest". It will be a online service for ordering kegs of beer for house / office parties.

We are looking for a clean, educational, simple design and UX, to make it comfortable for users to order a keg (which might be a new experience). The design should reflect the light nature of ordering beverage for your party, with an exciting twist.

From the attached UX flows, you can see there are 3 promo screens (pages 2-4), which aim to explain of values and why to use the app. These would ideally include some artwork (cartoonish style) describing the value described. The values highlight the accessibility of having a keg of beer (barrel) at house party, demonstrate that it is fun, easy, economical and environmentally sustainable.

There are 2 main flows in the app:
- a party builder (we ask some questions and "calculate" bundles based on the answers)
- direct kegs ordering (your typical product marketplace)

Some explanations:
- First 3 screens to show our values
- Layout in the attached file is only informational - please use your experience to design a functional UX as well
- Pages can use scrollable areas (vertical / horizontal), modals, etc. We will use FluxFrame so you can use those components in your design.
- Animation screen, when the party is being calculated (would be nice)
- The payment Screen will use the default Paxel payment sheet component (incl. Orchid / Zentry pay or credit card info)
- There is no logo yet, you can use just simple text on the splash screen
- There is no log-in functionality, so don't bother including login/signup screen or a profile area in the app
- for images of beers / breweries, you can use logo of https://www.harlowmeadales.example/ or similar (not actually images of beers)
- some of the offered beers / breweries / bundles might be Featured or otherwise prioritised, so it should be shown in the design

Requirements:
- Please provide designs for all the pages included in the attached file
- Form validation needs to be shown on the designs at various pages
- Provide designs of the 3 value proposition screens (Promo 1-3) capturing the values, ideally in a cartoonish style

Target Market(s)

Households

Industry/Entity Type

Food and beverage, delivery

Font styles to use
Sans Serif

Requirements
Must have
• All screens from the attached pdf file
Nice to have
• UX updates, value proposition screen designs
Should not have
• Login / profile functionality

```html
<!DOCTYPE html>
<html lang="en">
<head>
<meta charset="utf-8">
<title>Tapfold Nest – Value Screens</title>
<link rel="stylesheet" href="https://fonts.googleapis.com/css2?family=Poppins:wght@400;600&family=Sniglet:wght@800&display=swap">
<style>
  :root {
    --orange: #f28a13;
    --orange-deep: #ea6a0c;
    --orange-soft: #fbb24a;
    --party-red: #e2473c;
    --party-blue: #3a6fc4;
    --globe-blue: #3aa7dc;
    --globe-green: #4aa845;
    --piggy-pink: #f7b9bf;
    --ink: #1b1b1b;
    --frame: #0d0d0d;
    --screen: #ffffff;
    --dot-off: #c9c9c9;
    --page: #f4f1ec;
  }
  * { box-sizing: border-box; margin: 0; padding: 0; }
  html, body { width: 1200px; height: 812px; overflow: hidden; }
  body {
    background: var(--page);
    font-family: "Poppins", sans-serif;
    color: var(--ink);
  }
  .board {
    width: 1200px; height: 812px;
    display: flex; justify-content: center; align-items: center; gap: 26px;
  }
  .phone {
    width: 352px; height: 740px;
    border: 10px solid var(--frame);
    border-radius: 44px;
    background: var(--screen);
    position: relative;
    overflow: hidden;
  }
  .status-bar {
    position: absolute; top: 14px; left: 28px; right: 24px;
    display: flex; justify-content: space-between; align-items: center;
    font-size: 13px; font-weight: 600;
  }
  .status-icons { display: flex; gap: 4px; align-items: center; }
  .artwork {
    position: absolute; top: 70px; left: 16px; right: 16px; height: 268px;
    border-radius: 38% 62% 46% 54% / 50% 40% 60% 50%;
  }
  .artwork.party {
    background: linear-gradient(135deg, var(--orange-soft) 0%, var(--orange) 40%, var(--party-blue) 75%, var(--party-red) 100%);
  }
  .artwork.cheers {
    background: linear-gradient(135deg, var(--orange-deep) 0%, var(--orange) 45%, var(--orange-soft) 70%, var(--party-blue) 100%);
  }
  .artwork.savings {
    background: linear-gradient(120deg, var(--globe-blue) 0%, var(--globe-green) 30%, var(--orange) 55%, var(--piggy-pink) 85%);
  }
  .screen-title {
    position: absolute; top: 390px; left: 0; right: 0;
    text-align: center;
    font-family: "Sniglet", sans-serif; font-weight: 800;
    font-size: 16px; color: var(--orange);
    text-transform: uppercase; letter-spacing: 0.2px;
  }
  .screen-copy {
    position: absolute; top: 432px; left: 26px; right: 20px;
    font-size: 11.8px; line-height: 1.45;
  }
  .screen-copy p { margin-bottom: 16px; }
  .screen-copy strong { font-weight: 600; }
  .pager {
    position: absolute; top: 676px; left: 26px; display: flex; gap: 5px; align-items: center;
  }
  .pager span { width: 5px; height: 5px; border-radius: 50%; background: var(--dot-off); }
  .pager span.active { width: 8px; height: 8px; background: var(--orange); }
  .next-action {
    position: absolute; top: 668px; right: 26px;
    font-size: 12.5px; font-weight: 600; color: var(--orange); text-transform: uppercase;
  }
  .home-indicator {
    position: absolute; bottom: 8px; left: 50%; transform: translateX(-50%);
    width: 120px; height: 4px; border-radius: 2px; background: var(--frame);
  }
</style>
</head>
<body>
<main class="board">

  <section class="phone">
    <div class="status-bar"><span>9:41</span>
      <span class="status-icons">
        <svg width="16" height="10" viewBox="0 0 16 10"><rect x="0" y="7" width="3" height="3" fill="#111"/><rect x="4" y="5" width="3" height="5" fill="#111"/><rect x="8" y="3" width="3" height="7" fill="#111"/><rect x="12" y="0" width="3" height="10" fill="#111"/></svg>
        <svg width="14" height="10" viewBox="0 0 14 10"><path d="M1 3.5a9 9 0 0 1 12 0M3.3 5.8a5.6 5.6 0 0 1 7.4 0" stroke="#111" stroke-width="1.6" fill="none"/><circle cx="7" cy="8.6" r="1.3" fill="#111"/></svg>
        <svg width="22" height="10" viewBox="0 0 22 10"><rect x="0.5" y="0.5" width="19" height="9" rx="2" fill="none" stroke="#111"/><rect x="2" y="2" width="16" height="6" rx="1" fill="#111"/><rect x="20.3" y="3" width="1.5" height="4" fill="#111"/></svg>
      </span>
    </div>
    <div class="artwork party" role="img" aria-label="Cartoon illustration: a group of friends cheering and dancing beside a wooden beer keg, with balloons and confetti on an orange splash"></div>
    <h2 class="screen-title">Throw a Bash</h2>
    <div class="screen-copy">
      <p>Who loves a party? We all love a party, but we don't all love having to plan for one.</p>
      <p>Are you over the anxiety that comes with being the hostess with the mostess?</p>
      <p>Want to make sure your guests are sufficiently fed and watered?</p>
      <p>Well when it comes to beer drinkers, we got you covered!</p>
    </div>
    <div class="pager"><span class="active"></span><span></span><span></span></div>
    <span class="next-action">Next</span>
    <div class="home-indicator"></div>
  </section>

  <section class="phone">
    <div class="status-bar"><span>9:41</span>
      <span class="status-icons">
        <svg width="16" height="10" viewBox="0 0 16 10"><rect x="0" y="7" width="3" height="3" fill="#111"/><rect x="4" y="5" width="3" height="5" fill="#111"/><rect x="8" y="3" width="3" height="7" fill="#111"/><rect x="12" y="0" width="3" height="10" fill="#111"/></svg>
        <svg width="14" height="10" viewBox="0 0 14 10"><path d="M1 3.5a9 9 0 0 1 12 0M3.3 5.8a5.6 5.6 0 0 1 7.4 0" stroke="#111" stroke-width="1.6" fill="none"/><circle cx="7" cy="8.6" r="1.3" fill="#111"/></svg>
        <svg width="22" height="10" viewBox="0 0 22 10"><rect x="0.5" y="0.5" width="19" height="9" rx="2" fill="none" stroke="#111"/><rect x="2" y="2" width="16" height="6" rx="1" fill="#111"/><rect x="20.3" y="3" width="1.5" height="4" fill="#111"/></svg>
      </span>
    </div>
    <div class="artwork cheers" role="img" aria-label="Cartoon illustration: two smiling friends clinking beer mugs, with a calendar and a party popper on an orange splash"></div>
    <h2 class="screen-title">More Party, Less Planning</h2>
    <div class="screen-copy">
      <p>No more last minute runs to the bottle shop, supermarket or local wholesalers.</p>
      <p>No more back breaking journeys carrying heavy beer bottles and cans across your neighbourhood.</p>
      <p>No more worries about fridge capacity and no more warm beers for your guests.</p>
    </div>
    <div class="pager"><span></span><span class="active"></span><span></span></div>
    <span class="next-action">Next</span>
    <div class="home-indicator"></div>
  </section>

  <section class="phone">
    <div class="status-bar"><span>9:41</span>
      <span class="status-icons">
        <svg width="16" height="10" viewBox="0 0 16 10"><rect x="0" y="7" width="3" height="3" fill="#111"/><rect x="4" y="5" width="3" height="5" fill="#111"/><rect x="8" y="3" width="3" height="7" fill="#111"/><rect x="12" y="0" width="3" height="10" fill="#111"/></svg>
        <svg width="14" height="10" viewBox="0 0 14 10"><path d="M1 3.5a9 9 0 0 1 12 0M3.3 5.8a5.6 5.6 0 0 1 7.4 0" stroke="#111" stroke-width="1.6" fill="none"/><circle cx="7" cy="8.6" r="1.3" fill="#111"/></svg>
        <svg width="22" height="10" viewBox="0 0 22 10"><rect x="0.5" y="0.5" width="19" height="9" rx="2" fill="none" stroke="#111"/><rect x="2" y="2" width="16" height="6" rx="1" fill="#111"/><rect x="20.3" y="3" width="1.5" height="4" fill="#111"/></svg>
      </span>
    </div>
    <div class="artwork savings" role="img" aria-label="Cartoon illustration: a woman dropping a gold coin into a pink piggy bank in front of a green and blue globe, with stacked coins"></div>
    <h2 class="screen-title">Save Money and the Planet</h2>
    <div class="screen-copy">
      <p>Finally a <strong>cost efficient, environmentally sustainable, no hassle</strong> and <strong>fun</strong> way to keep all the beer drinkers at your party smiling.</p>
      <p>Our service enables you to throw a keg party of your dreams by removing the logistical challenges so you and your guests can focus on having a good time.</p>
      <p>Never worry about your beer supply again.</p>
    </div>
    <div class="pager"><span></span><span></span><span class="active"></span></div>
    <span class="next-action">Continue</span>
    <div class="home-indicator"></div>
  </section>

</main>
</body>
</html>
```